website for cartnest- Almond Valet. Natural Peanut Butter Mixer

I need a website for cartnest for my invention...The AlmondValet. ( Registered trademark)
They are kitchen accessories for mixing Natural peanut butter (9 mixing hooks). Natural peanut butter separates with oil floating to the top when it sits on the shelf. Very hard and messy to mix it in manually.

My hook is compatible with 8 popular brand name electric hand mixers, plus 1/4” HEX universal drill bit. (9 total)

The mixing Hook part that goes into the nut butter is all the same for each hook, it’s just locking interface changes for each hook. I will supply a close up photo for each hook lock mechanism. ( leave blank until Thursday next week)
Brands are: Grey and Mallory, Vexomart, Corwin Harbor, StoveMate, Pryle, Dunmore Vaxil, Glowfield Modern, Glowfield Retro.
Plus 1/4” HEX quick lock drill bit.

I would like to inspire with complementary healthy peanut butter snack images..as peanut butter is pretty brown!!
There are lots of beautiful stock photos of peanut butter snacks on lensvault or Pixbarn. Samples included in my files. My logo needs to have Registered trade Mark R in circle ⭕️ added to end of logo.
Plus I would like a couple of smiling moms with kids eating peanut butter.

Target Market(s)

North American health food minded people.

Coding

Coded - Design and coding required

Number of Pages Required

5+ page

Font styles to use
Sans Serif

Colors
ffffff
ec1f27
f78f20
9bcb3c

Requirements
Must have
• I have about 6 sections in my 1 page website to design....page 7 thru 15 are all the same with just photo and brand name changes and list of model numbers compatible, for each different mixing hook.

I want my headline to rotate with 3 changing words.
Natural Peanut Butter
1) Mixed Perfectly 2) Better Tasting 3) Hassle-Free

Want to add shop now button on all pages.

Clean white background. I like shadow colour boxes behind clusters of 2-3 photos. Contemporary look.
I can type and upload blog pages soon so you don’t have to type them in. Just add a few photos.
Patented Design!!! Important to add so copy cats don’t copy.
Nice to have
• Complementary 3 colour palette that doesn’t change. Red being one.
Open to seeing other colour palettes.
Should not have
• Logos of any brand names. Just written in a clear black font consistent for all.

```html
<!DOCTYPE html>
<html lang="en">
<head>
<meta charset="utf-8">
<title>Almond Valet – Natural Peanut Butter Mixer</title>
<link rel="stylesheet" href="https://fonts.googleapis.com/css2?family=Orbitron:wght@700;800&family=Poppins:wght@400;500;600;700&display=swap">
<style>
:root{
  --brown:#8a5a50;
  --brown-dark:#7a4b42;
  --salmon:#f7ab8c;
  --salmon-edge:#e99c7e;
  --blush:#fbe6dd;
  --gold:#f5b300;
  --white:#ffffff;
  --text:#5a4440;
  --grey-circle:#efefef;
}
*{box-sizing:border-box;margin:0;padding:0}
html,body{width:1200px;height:4337px;overflow:hidden;background:var(--white)}
body{position:relative;font-family:"Poppins",sans-serif;color:var(--text)}
.abs{position:absolute}
.bg{position:absolute;left:0;top:0}
.display{font-family:"Orbitron",sans-serif;font-weight:800;text-transform:uppercase;letter-spacing:1px}
.center{left:0;width:1200px;text-align:center}
.pill{display:inline-block;border-radius:20px;font-weight:700;text-transform:uppercase;font-family:"Poppins",sans-serif}
.photo{position:absolute;border-radius:50%}

/* header */
.logo{display:flex;align-items:center;gap:10px}
.logo-dot{width:34px;height:34px;border-radius:50%;background:var(--brown)}
.logo-name{font-weight:600;font-size:22px;letter-spacing:3px;color:var(--brown);text-transform:uppercase}
.top-nav{right:88px;top:32px;display:flex;gap:26px;font-size:13px;font-weight:600;color:#333}

/* hero */
.hero-kicker{top:184px;font-size:22px;color:var(--brown);font-family:"Poppins",sans-serif;font-weight:600;letter-spacing:1px}
.hero-title{top:205px;font-size:58px;color:var(--gold)}
.hero-shop{top:276px}
.hero-shop .pill{background:var(--brown);color:var(--white);font-size:14px;padding:5px 26px}

/* how it works */
.how-title{top:948px;font-size:38px;color:var(--white)}
.steps{top:1040px;left:120px;width:1000px;display:flex;justify-content:space-between}
.step{width:240px;text-align:center;color:var(--white)}
.step-num{font-family:"Orbitron",sans-serif;font-weight:800;font-size:62px;color:var(--salmon);line-height:1}
.step-text{font-size:15px;line-height:1.3;margin-top:10px}
.bump-shop{left:540px;top:1322px;width:120px;text-align:center;font-weight:700;font-size:19px;color:var(--brown);letter-spacing:1px}

/* price */
.price{top:1455px;font-family:"Poppins",sans-serif;font-weight:700;font-size:80px;color:var(--brown-dark);line-height:1}
.price small{font-size:22px}
.coupon-title{top:1547px;font-size:24px;color:var(--brown)}
.coupon-note{top:1576px;font-size:18px;color:var(--brown)}
.signup{display:flex;width:518px;height:40px;border-radius:20px;background:var(--white);overflow:hidden}
.signup span{flex:1;padding-left:26px;line-height:40px;font-size:13px;color:#333}
.signup b{width:156px;background:var(--brown);color:var(--white);border-radius:20px;text-align:center;line-height:40px;font-size:16px;text-transform:uppercase}

/* brands */
.brand{position:absolute;border-radius:50%;display:flex;align-items:center;justify-content:center;font-weight:600;color:#111;text-align:center;line-height:1.1}
.choose-title{top:2078px;font-size:40px;color:var(--brown);line-height:1.05}

/* natural */
.natural-title{top:2530px;font-size:38px;color:var(--brown)}
.natural-sub{top:2578px;font-size:19px;color:var(--brown)}
.jar{position:absolute;border-radius:16px}

/* reviews */
.reviews-title{top:3048px;font-size:38px;color:var(--brown)}
.card{position:absolute;top:3117px;width:334px;height:182px;background:var(--white);box-shadow:0 4px 18px rgba(0,0,0,.1);padding:22px 22px}
.card::after{content:"";position:absolute;left:26px;bottom:-18px;border-left:18px solid var(--white);border-bottom:18px solid transparent}
.card-head{display:flex;align-items:center;gap:14px}
.avatar{width:42px;height:42px;border-radius:50%;background:#c9a18f}
.card-name{font-weight:600;font-size:15px;color:#222;text-transform:uppercase;line-height:1.1}
.card-role{font-size:12px;color:#444}
.card-text{font-size:12.5px;line-height:1.5;margin-top:10px;color:#333}
.stars{color:var(--gold);font-size:15px;letter-spacing:3px;margin-top:2px}

/* bottom signup */
.ship-title{top:3600px;font-size:38px;color:var(--brown)}
.ship-sub{top:3648px;font-size:18px;color:var(--brown)}
.hungry{top:3955px;left:330px;display:flex;align-items:center;gap:28px}
.hungry h2{font-size:38px;font-weight:600;color:var(--white);letter-spacing:1px}
.hungry .pill{background:var(--salmon);color:var(--white);font-size:16px;padding:4px 26px}

/* footer */
.footer-logo{left:128px;top:4140px}
.footer-logo .logo-dot{background:var(--white)}
.footer-logo .logo-name{color:var(--white);font-size:24px}
.foot-col{color:var(--white);font-size:16px;line-height:28.5px}
.foot-col h4{font-weight:600;font-size:17px}
.foot-email{width:236px;height:32px;border-radius:16px;background:var(--white);color:#333;font-size:13px;padding-left:20px;line-height:32px;margin-top:6px;position:relative}
.foot-email svg{position:absolute;right:14px;top:9px}
.foot-rule{left:88px;top:4292px;width:1024px;height:1px;background:rgba(255,255,255,.35)}
.copyright{left:88px;top:4305px;font-size:14px;color:var(--white);font-weight:500}
.socials{right:90px;top:4308px;display:flex;gap:5px}
.socials i{width:11px;height:11px;background:var(--white);border-radius:2px;display:block}
.to-top{left:1134px;top:4256px;width:30px;height:30px;border-radius:50%;background:var(--salmon)}
</style>
</head>
<body>

<svg class="bg" width="1200" height="4337" viewBox="0 0 1200 4337" aria-hidden="true">
  <!-- hero brown band -->
  <path d="M0,650 C200,730 420,720 620,660 C820,600 1000,560 1200,500 L1200,1440 L0,1440 Z" fill="var(--salmon-edge)"/>
  <path d="M0,680 C200,760 420,745 620,690 C820,630 1000,590 1200,535 L1200,1440 L0,1440 Z" fill="var(--brown)"/>
  <!-- salmon coupon band -->
  <path d="M0,1330 C180,1350 330,1380 480,1400 L720,1400 C860,1410 1050,1400 1200,1370 L1200,1830 C1100,1860 1000,1800 900,1760 C700,1690 300,1670 0,1770 Z" fill="var(--salmon)"/>
  <circle cx="600" cy="1338" r="106" fill="var(--salmon)"/>
  <!-- blush band -->
  <path d="M0,2360 C200,2300 400,2330 600,2360 C800,2390 1000,2330 1200,2320 L1200,2690 C1000,2640 800,2690 600,2680 C400,2670 200,2640 0,2690 Z" fill="var(--blush)"/>
  <!-- bottom salmon -->
  <path d="M0,3420 C200,3360 400,3400 620,3440 C850,3480 1050,3420 1200,3380 L1200,4337 L0,4337 Z" fill="var(--salmon)"/>
  <!-- bottom brown -->
  <path d="M0,3860 C250,3800 500,3780 760,3840 C950,3880 1100,3850 1200,3820 L1200,4337 L0,4337 Z" fill="var(--brown)"/>
</svg>

<!-- header -->
<div class="abs logo" style="left:508px;top:22px">
  <span class="logo-dot"></span><span class="logo-name">Almond Valet</span>
</div>
<nav class="abs top-nav"><span>BLOG</span><span>HELP</span></nav>

<!-- hero -->
<div class="abs center hero-kicker">NATURAL PEANUT BUTTER</div>
<h1 class="abs center display hero-title">Mixed Perfectly</h1>
<div class="abs center hero-shop"><span class="pill">Shop now</span></div>

<div class="photo" role="img" aria-label="Mixing hook spiralling into an open jar of dripping peanut butter" style="left:470px;top:310px;width:260px;height:560px;border-radius:40%;background:linear-gradient(180deg,#d8c2a0,#e2a640 50%,#c98a2c)"></div>
<div class="photo" role="img" aria-label="Toast spread with peanut butter" style="left:-40px;top:330px;width:120px;height:230px;border-radius:40%;background:linear-gradient(135deg,#c48538,#e0a456)"></div>
<div class="photo" role="img" aria-label="Swirl of peanut butter" style="left:236px;top:336px;width:86px;height:86px;background:radial-gradient(#e6b078,#c9894a)"></div>
<div class="photo" role="img" aria-label="Peanut butter on a spoon" style="left:1130px;top:205px;width:90px;height:100px;background:radial-gradient(#e7a95a,#c98633)"></div>
<div class="photo" role="img" aria-label="Peanuts, banana slices and a peanut butter bowl" style="left:1010px;top:430px;width:200px;height:220px;border-radius:30%;background:linear-gradient(160deg,#e5c08a,#8e6a4c 70%,#f0dcae)"></div>
<div class="photo" role="img" aria-label="Mother and child eating peanut butter snacks, faded into the background" style="left:160px;top:760px;width:860px;height:480px;border-radius:40%;background:radial-gradient(rgba(255,255,255,.07),rgba(255,255,255,0) 70%)"></div>
<div class="photo" role="img" aria-label="Steel mixing hook" style="left:190px;top:760px;width:50px;height:255px;border-radius:20px;background:linear-gradient(90deg,#5c6670,#c9d0d5,#5c6670);opacity:.8"></div>

<!-- how it works -->
<h2 class="abs center display how-title">How it works</h2>
<div class="abs steps">
  <div class="step"><div class="step-num">01</div><div class="step-text">Use your own hand<br>mixer or drill</div></div>
  <div class="step"><div class="step-num">02</div><div class="step-text">Thin-2 mm Stainless Steel hook<br>mixes without displacing oil</div></div>
  <div class="step"><div class="step-num">03</div><div class="step-text">Mix it right in your<br>store-bought jar.</div></div>
  <div class="step"><div class="step-num">04</div><div class="step-text">Arrow Tip breaks up settled nuts<br>creating top to bottom flow.</div></div>
</div>
<div class="photo" role="img" aria-label="Scoop of peanut butter with peanuts" style="left:0;top:1195px;width:210px;height:160px;background:radial-gradient(#e9a65a,#c27f35)"></div>
<div class="photo" role="img" aria-label="Bowl of peanut butter ice cream" style="left:818px;top:1238px;width:322px;height:220px;border-radius:50% 50% 0 0;background:radial-gradient(#f3e2d2,#e4c6ac)"></div>
<div class="abs bump-shop">SHOP NOW</div>

<!-- price -->
<div class="photo" role="img" aria-label="Jar of natural peanut butter with black lid" style="left:88px;top:1470px;width:178px;height:270px;border-radius:22px;background:linear-gradient(180deg,#2d2a28 0 14%,#c48a3a 14%,#e1a64e 60%,#b67a2f)"></div>
<div class="photo" role="img" aria-label="Open jar of peanut butter surrounded by peanuts" style="left:780px;top:1470px;width:340px;height:330px;border-radius:40%;background:radial-gradient(#e7b062,#c89355 60%,#d9ac72)"></div>
<div class="abs center price">$19.99<small>USD</small></div>
<div class="abs center display coupon-title">Sign up for free shipping coupon</div>
<div class="abs center coupon-note">(Valid in USA and Canada only)</div>
<div class="abs signup" style="left:342px;top:1614px"><span>Enter your email address</span><b>Sign up</b></div>

<!-- brands -->
<div class="brand" style="left:162px;top:1908px;width:92px;height:92px;background:#fbefef;color:var(--brown);font-size:13px">Glowfield</div>
<div class="brand" style="left:-10px;top:1980px;width:190px;height:190px;background:#fdeee6;font-size:17px;color:#222">Grey and<br>Mallory</div>
<div class="brand" style="left:214px;top:2015px;width:122px;height:122px;background:var(--grey-circle);font-size:16px">Vexomart</div>
<div class="photo" role="img" aria-label="Stand mixer" style="left:0;top:2198px;width:98px;height:98px;background:var(--grey-circle)"></div>
<div class="brand" style="left:142px;top:2196px;width:138px;height:138px;background:#f5e6e6;color:var(--brown);font-size:14px">StoveMate</div>
<div class="brand" style="left:886px;top:1946px;width:178px;height:178px;background:var(--grey-circle);font-size:17px">Corwin<br>Harbor</div>
<div class="brand" style="left:1094px;top:1966px;width:124px;height:124px;background:#e8f0f8;color:#1d4f91;font-size:20px">Pryle</div>
<div class="brand" style="left:886px;top:2144px;width:126px;height:126px;background:var(--grey-circle);font-size:13px">Dunmore<br>Vaxil</div>
<div class="photo" role="img" aria-label="Drill bit in a drill chuck" style="left:1050px;top:2126px;width:152px;height:152px;background:linear-gradient(135deg,#f3f3f3,#e2e2e2)"></div>
<h2 class="abs center display choose-title">Choose your<br>hook how</h2>

<!-- natural -->
<div class="photo" role="img" aria-label="Steel mixing hook" style="left:1000px;top:2300px;width:70px;height:300px;border-radius:30px;background:linear-gradient(90deg,#6a747c,#d6dbde,#6a747c)"></div>
<h2 class="abs center display natural-title">Mixes in all natural</h2>
<div class="abs center display natural-sub">Nut butters right in their own jars.</div>
<div class="jar" role="img" aria-label="Jar of cashew butter" style="left:130px;top:2692px;width:108px;height:205px;background:linear-gradient(180deg,#e7b24a,#fdf3d9 40%,#e4a740)"></div>
<div class="jar" role="img" aria-label="Jar of macadamia nut butter" style="left:282px;top:2696px;width:120px;height:200px;background:linear-gradient(180deg,#b7b08e,#bfe0d6 45%,#8f8a70)"></div>
<div class="jar" role="img" aria-label="Large jar of almond butter" style="left:455px;top:2634px;width:290px;height:300px;border-radius:28px;background:linear-gradient(180deg,#f4f0ea 0 10%,#c4945a 10%,#e9c596 55%,#a77445)"></div>
<div class="jar" role="img" aria-label="Jar of tahini sesame paste" style="left:795px;top:2692px;width:125px;height:205px;background:linear-gradient(180deg,#f1cf74,#efe6d0 45%,#d8c29a)"></div>
<div class="jar" role="img" aria-label="Jar of hazelnut butter" style="left:975px;top:2694px;width:135px;height:205px;background:linear-gradient(180deg,#e6e6e6 0 14%,#8a4a2c 14%,#6e3a22)"></div>

<!-- reviews -->
<h2 class="abs center display reviews-title">What people are saying...</h2>
<div class="card" style="left:89px">
  <div class="card-head"><div class="avatar" role="img" aria-label="Reviewer portrait"></div><div><div class="card-name">Jordan Hale</div><div class="card-role">Co Founder</div></div></div>
  <p class="card-text">"Lorem Ipsum is simply dummy text of the printing and typesetting industry. Lorem Ipsum has been the industry's standard dummy"</p>
  <div class="stars">★★★★★</div>
</div>
<div class="card" style="left:432px">
  <div class="card-head"><div class="avatar" role="img" aria-label="Reviewer portrait"></div><div><div class="card-name">Jordan Hale</div><div class="card-role">Co Founder</div></div></div>
  <p class="card-text">"Lorem Ipsum is simply dummy text of the printing and typesetting industry. Lorem Ipsum has been the industry's standard dummy"</p>
  <div class="stars">★★★★★</div>
</div>
<div class="card" style="left:776px">
  <div class="card-head"><div class="avatar" role="img" aria-label="Reviewer portrait"></div><div><div class="card-name">Jordan Hale</div><div class="card-role">Co Founder</div></div></div>
  <p class="card-text">"Lorem Ipsum is simply dummy text of the printing and typesetting industry. Lorem Ipsum has been the industry's standard dummy"</p>
  <div class="stars">★★★★★</div>
</div>

<!-- bottom signup -->
<h2 class="abs center display ship-title">Sign up for free shipping + get</h2>
<div class="abs center ship-sub">12 Natural Peanut Butter Mixing Hacks!....That actually Work</div>
<div class="abs signup" style="left:342px;top:3678px"><span>Enter your email address</span><b>Sign up</b></div>

<div class="abs hungry"><h2>Hungry for more?</h2><span class="pill">Shop now</span></div>

<!-- footer -->
<div class="abs logo footer-logo"><span class="logo-dot"></span><span class="logo-name">Almond Valet</span></div>
<div class="abs foot-col" style="left:446px;top:4096px"><div>Shop</div><div>Hooks</div><div>BLogs</div></div>
<div class="abs foot-col" style="left:628px;top:4096px"><div>Help</div><div>Peanut Butter</div><div>Recipes</div><div>Return +</div><div>Warranty</div></div>
<div class="abs foot-col" style="left:836px;top:4098px">
  <h4>Contact Us</h4>
  <div>info@almondvalet.example</div>
  <h4>Signup for free shippings</h4>
  <div class="foot-email">Email address
    <svg width="16" height="14" viewBox="0 0 16 14"><path d="M0,6 L16,0 L11,14 L8,8 Z" fill="var(--salmon)"/></svg>
  </div>
</div>
<div class="abs to-top"></div>
<div class="abs foot-rule"></div>
<div class="abs copyright">Copyright 2021 | All Rights Reserved</div>
<div class="abs socials"><i></i><i></i></div>

</body>
</html>
```